SkyvoraQ Business Cards and Stationary Design

Need a design for our business cards and stationary. I want to carry on the theme of the logo. I want the business cards to have a design on the back. I would like the business cards and the stationary to carry the same theme, design scheme, and branding

Target Market(s)

Airlines and Maintenance Facilities

Industry/Entity Type

Aviation

Contact Information for Business Card

Name
Position Title
Address: 4827 Tollbeck Lane, Marlow Bay, Oregon, 97418
Office Number
Mobile Number
Email
Website

Font styles to use
Serif
Sans Serif

Colors

Designer to choose colors to be used in the design.

```html
<!DOCTYPE html>
<html lang="en">
<head>
<meta charset="utf-8">
<title>SkyvoraQ Business Card</title>
<link rel="stylesheet" href="https://fonts.googleapis.com/css2?family=Montserrat:wght@400;700;800&family=Open+Sans:wght@400;600&display=swap">
<style>
  :root {
    --backdrop: #1c1c1e;
    --card-white: #ffffff;
    --card-black: #0c0c0e;
    --navy: #0d2a66;
    --brand-blue: #1f6fc4;
    --ink: #111111;
    --muted-blue: #2b64b8;
  }
  * { margin: 0; padding: 0; box-sizing: border-box; }
  html, body {
    width: 1200px; height: 900px; overflow: hidden;
    background: var(--backdrop);
  }
  .canvas { position: relative; width: 1200px; height: 900px; }

  .card {
    position: absolute;
    width: 580px; height: 350px;
    border-radius: 26px;
    box-shadow: 0 18px 40px rgba(0,0,0,.55);
  }

  /* back of card */
  .card-back {
    left: 580px; top: 100px;
    background: var(--card-black);
    display: flex; flex-direction: column; align-items: center; justify-content: center;
    gap: 28px;
  }
  .brand {
    display: flex; align-items: center; gap: 16px;
    font-family: "Montserrat", sans-serif; font-weight: 800;
    text-transform: uppercase; letter-spacing: 4px;
    white-space: nowrap;
  }
  .brand-mark { border-radius: 50%; border: 5px solid currentColor; flex: none; }
  .card-back .brand { color: var(--brand-blue); font-size: 46px; }
  .card-back .brand-mark { width: 64px; height: 64px; }
  .website {
    font-family: "Open Sans", sans-serif; font-size: 17px;
    letter-spacing: 3px; color: var(--brand-blue);
  }

  /* front of card */
  .card-front {
    left: 40px; top: 480px;
    background: var(--card-white);
    display: flex; align-items: center;
    padding: 0 22px 0 30px;
  }
  .card-front .brand { color: var(--navy); font-size: 27px; letter-spacing: 3px; gap: 10px; }
  .card-front .brand-mark { width: 38px; height: 38px; border-width: 4px; }
  .logo-area { width: 262px; display: flex; justify-content: center; flex: none; }
  .divider { width: 2px; height: 200px; background: var(--navy); margin: 0 22px 0 8px; flex: none; }
  .details { font-family: "Open Sans", sans-serif; color: var(--ink); white-space: nowrap; }
  .name {
    font-family: "Montserrat", sans-serif; font-weight: 800;
    font-size: 24px; line-height: 1; color: var(--ink);
  }
  .title {
    font-family: "Montserrat", sans-serif; font-weight: 400;
    font-size: 15px; color: var(--muted-blue); margin: 4px 0 14px;
  }
  .contact-list { list-style: none; font-size: 13.5px; line-height: 1.4; }
  .contact-list li { display: flex; align-items: flex-start; gap: 9px; margin-bottom: 6px; }
  .contact-list svg { width: 14px; height: 14px; flex: none; margin-top: 3px; fill: var(--navy); }
</style>
</head>
<body>
<main class="canvas">

  <section class="card card-back" aria-label="Back of business card">
    <div class="brand"><span class="brand-mark"></span>SkyvoraQ</div>
    <div class="website">www.yourwebsite.com</div>
  </section>

  <section class="card card-front" aria-label="Front of business card">
    <div class="logo-area">
      <div class="brand"><span class="brand-mark"></span>SkyvoraQ</div>
    </div>
    <div class="divider"></div>
    <div class="details">
      <h1 class="name">YOUR NAME</h1>
      <p class="title">JOB TITLE</p>
      <ul class="contact-list">
        <li>
          <svg viewBox="0 0 16 16"><path d="M4 1h8a1 1 0 0 1 1 1v12a1 1 0 0 1-1 1H4a1 1 0 0 1-1-1V2a1 1 0 0 1 1-1zm1 2v9h6V3z"/></svg>
          000 000 0000
        </li>
        <li>
          <svg viewBox="0 0 16 16"><path d="M3.5 1.5l2.5 0 1 3.5-1.6 1.2a9 9 0 0 0 4.4 4.4L11 9l3.5 1v2.5c0 1-1 2-2 2C7 14.5 1.5 9 1.5 3.5c0-1 1-2 2-2z"/></svg>
          (310) 555-5555
        </li>
        <li>
          <svg viewBox="0 0 16 16"><path d="M1 3h14v10H1zm1.5 1.2V5l5.5 4 5.5-4v-.8z"/></svg>
          youremail@xyz.com
        </li>
        <li>
          <svg viewBox="0 0 16 16"><path d="M8 0a5 5 0 0 1 5 5c0 4-5 11-5 11S3 9 3 5a5 5 0 0 1 5-5zm0 3a2 2 0 1 0 0 4 2 2 0 0 0 0-4z"/></svg>
          <span>4827 Tollbeck Lane, Marlow Bay,<br>Oregon, 97418</span>
        </li>
      </ul>
    </div>
  </section>

</main>
</body>
</html>
```